Professional and dynamic bifold brochure for Radiology practice

We need a tabloid-sized bifold brochure (each panel 8.5"x11") introducing our practice and what we offer. Images will include diagnostic machines like MRI, Ultrasound and CAT scan, the radiology images themselves and happy professionals working with happy patients. While we have two centers, the largest one is in Boca Raton and contains the latest equipment. We do NOT need to use all or even most of the attached images. We do want stock photos of happy people in the clinical setting

Target Market(s)

Referring physicians

Industry/Entity Type

Medical

Font styles to use
Sans Serif

Colors
0054AA
0677BA
7BADD7
CADEEF
E8F1F8

Requirements
Must have
• a good mix of text and graphics, and the images must form a good balance between people and machines/site/anatomy. Also cleaned-up images of the facility if possible and a location map if there is room
Nice to have
• A good flow from panel to panel, segmented content and imagery to match
Should not have
• Dark themes, odd shapes, cluttered content, confusing flow

```html
<!DOCTYPE html>
<html lang="en">
<head>
<meta charset="utf-8">
<title>Radiology Practice Bifold Brochure – Inside Spread</title>
<link rel="stylesheet" href="https://fonts.googleapis.com/css2?family=Montserrat:wght@400;500;700&display=swap">
<style>
  :root{
    --navy:#0054AA;
    --blue:#0677BA;
    --sky:#7BADD7;
    --mist:#CADEEF;
    --ice:#E8F1F8;
    --stage:#F7F7F7;
    --ink:#2F4A6E;
    --white:#FFFFFF;
  }
  *{box-sizing:border-box;margin:0;padding:0}
  html,body{width:1200px;height:1000px;overflow:hidden;background:var(--stage)}
  body{font-family:"Montserrat",Arial,sans-serif;color:var(--ink);position:relative}
  .spread{position:absolute;left:90px;top:170px;width:1020px;height:660px;display:flex;box-shadow:0 6px 24px rgba(0,0,0,.12)}
  .page{position:relative;width:510px;height:660px;overflow:hidden;background:linear-gradient(180deg,var(--ice) 0%,var(--mist) 100%)}
  .page--left{background:linear-gradient(160deg,var(--mist) 0%,var(--ice) 45%,var(--mist) 100%)}
  .page--left::after{content:"";position:absolute;right:0;top:0;width:18px;height:100%;background:linear-gradient(90deg,transparent,rgba(0,40,90,.12))}
  .page--right::before{content:"";position:absolute;left:0;top:0;width:18px;height:100%;background:linear-gradient(270deg,transparent,rgba(0,40,90,.12));z-index:3}
  .curves{position:absolute;inset:0;width:100%;height:100%}
  .photo{position:absolute;border-radius:2px;z-index:1}
  .photo--framed{border:5px solid var(--white);box-shadow:0 2px 8px rgba(0,40,90,.2)}
  .copy{position:absolute;z-index:2;font-size:10.5px;line-height:1.45}
  .copy p+p{margin-top:6px}
  .headline{color:var(--navy);font-weight:700;font-size:12.5px;line-height:1.35;margin-bottom:6px}
  .lead{color:var(--navy);font-weight:500;font-size:11.5px;line-height:1.45}
  .strong{color:var(--navy);font-weight:700}
  .rule{position:absolute;height:5px;background:var(--blue);z-index:2}
  .accent-bar{position:absolute;width:4px;background:var(--navy);z-index:2}
</style>
</head>
<body>
<main class="spread">

  <!-- Left inside panel -->
  <section class="page page--left">
    <svg class="curves" viewBox="0 0 510 660" aria-hidden="true">
      <path d="M0 300 C150 250 330 320 510 240 L510 300 C330 360 150 300 0 345Z" fill="#FFFFFF" opacity=".45"/>
      <path d="M0 0 H510 V95 C380 120 200 80 0 110Z" fill="#CADEEF" opacity=".6"/>
    </svg>

    <div class="photo photo--framed" style="left:22px;top:22px;width:92px;height:80px;background:radial-gradient(circle,#ffffff 30%,#dfe7ee 70%)" role="img" aria-label="White wide-bore MRI scanner on a light background"></div>

    <div class="copy lead" style="left:130px;top:18px;width:330px">
      We offer the latest 3 Tesla Wide bore Veltra MRI, 640-slice hyperfine low-dose CT, digital x-ray &amp; fluoroscopy, 3D/4D ultrasound, 3D Mammogram with tomosynthesis, body composition/DEXA, PET/CT and more.
    </div>

    <div class="photo" style="left:180px;top:112px;width:330px;height:118px;background:linear-gradient(100deg,#c9b6ad 0%,#6d8fb5 40%,#2e5a8a 70%,#9fb8cf 100%)" role="img" aria-label="Radiologist reviewing an x-ray film with a senior patient"></div>

    <div class="photo photo--framed" style="left:36px;top:150px;width:175px;height:118px;background:linear-gradient(160deg,#f2f4f5 0%,#cfd9e2 55%,#b8c7d5 100%)" role="img" aria-label="Patient lying in an MRI scanner"></div>

    <div class="rule" style="left:0;top:238px;width:180px"></div>
    <div class="rule" style="left:215px;top:232px;width:295px;background:var(--navy)"></div>

    <div class="accent-bar" style="left:40px;top:296px;height:90px"></div>
    <div class="copy" style="left:52px;top:292px;width:420px">
      <p class="headline">We cater to all specialties with customized protocols and specialty boarded Radiologists who are available to consult with.</p>
      <p>Whether your practice is orthopedics, neurology, ENT, internal medicine, chiropractic, podiatry, cardiology, oncology, OB/GYN, internal medicine, urology, nephrology, hepatology, vascular, sports medicine, pediatrics, geriatrics, bariatrics, endocrinology or dermatology, we are here for you and your patients.</p>
    </div>

    <div class="photo" style="left:0;top:430px;width:300px;height:230px;background:linear-gradient(120deg,#8c7a6e 0%,#d9d4cf 35%,#f0ede8 60%,#cfd6dd 100%)" role="img" aria-label="Smiling technologist with a happy patient beside imaging equipment"></div>
    <div class="photo photo--framed" style="left:285px;top:415px;width:225px;height:185px;background:linear-gradient(150deg,#e6ecf1 0%,#9fb3c6 50%,#4d6680 100%)" role="img" aria-label="Ultrasound exam in progress with monitor and keyboard"></div>
  </section>

  <!-- Right inside panel -->
  <section class="page page--right">
    <svg class="curves" viewBox="0 0 510 660" aria-hidden="true">
      <path d="M0 0 C120 30 170 5 250 0Z" fill="#7BADD7" opacity=".5"/>
      <path d="M0 410 C170 360 330 430 510 380 L510 660 L0 660Z" fill="#CADEEF" opacity=".7"/>
      <path d="M0 470 C160 420 330 480 510 440" fill="none" stroke="#FFFFFF" stroke-width="6" opacity=".6"/>
    </svg>

    <div class="photo photo--framed" style="left:30px;top:18px;width:165px;height:120px;background:linear-gradient(140deg,#f1f3f5 0%,#d6a3b6 45%,#c9d3dc 100%)" role="img" aria-label="Technologist positioning a patient for a mammogram"></div>
    <div class="photo" style="left:205px;top:0;width:305px;height:150px;background:linear-gradient(120deg,#eef0f2 0%,#e4c8bb 35%,#d5dbe1 65%,#9fb0c0 100%)" role="img" aria-label="Smiling technologist with a patient on the CT scanner table"></div>

    <div class="rule" style="left:0;top:158px;width:510px;background:var(--sky);height:4px"></div>

    <div class="copy" style="left:40px;top:178px;width:420px">
      <p class="headline">Cutting-edge equipment, highly experienced staff, unrivaled customer care.</p>
      <p>Fast same-day turnaround, detailed reports, online image access and a dedicated referral line. Fully HIPAA compliant, friendly bilingual staff, convenient hours and free parking. Most insurance plans accepted, with new plans added regularly.</p>
    </div>

    <div class="rule" style="left:60px;top:282px;width:450px;background:var(--navy);height:4px"></div>

    <div class="photo photo--framed" style="left:48px;top:296px;width:230px;height:150px;background:linear-gradient(130deg,#dfe3e6 0%,#b9a99e 40%,#f1f3f5 70%,#c7d0d8 100%)" role="img" aria-label="Doctor in white coat talking with a patient next to a scanner"></div>
    <div class="photo" style="left:288px;top:300px;width:222px;height:130px;background:linear-gradient(140deg,#f3f4f5 0%,#7fa6cf 45%,#3f6c9d 100%)" role="img" aria-label="Clinician helping a patient on a physical therapy table"></div>

    <div class="copy" style="left:40px;top:478px;width:430px;font-size:11px">
      <p>Our facilities are very modern, extraordinarily clean and built for comfort. <span class="strong">Our procedures are completed rapidly and we have minimal wait time.</span> All patients are treated with the utmost individualized care and respect, and any critical or notable findings are reported back to your referring physicians quickly and securely.</p>
    </div>
  </section>

</main>
</body>
</html>
```